Now Serving Louisville and Lexington KY

We need a postcard announcing our company now serves Louisville and Lexington KY. I would like the postcard to have the same appearance and message as our home page for our website www.swiftpaperdeliveryagentsonline.com

The front should include a skyline of Louisville on the front and incorporate our Bramblegate Dispatch Logo

The back of the postcard should incorporate the Wexmoor Inquiries logo with a brief bio of company founder Dan Pellworth

Target Market(s)

Attorneys and national process servers

Industry/Entity Type

It Company

Colors
3176b5

Requirements
Nice to have
• Louisville skyline

```html
<!DOCTYPE html>
<html lang="en">
<head>
<meta charset="utf-8">
<title>Now Serving Louisville and Lexington KY – Postcard</title>
<link rel="stylesheet" href="https://fonts.googleapis.com/css2?family=Libre+Baskerville&family=Montserrat:wght@700;800&family=Open+Sans:wght@700&family=Roboto+Condensed:wght@700&display=swap">
<style>
  :root {
    --paper: #ffffff;
    --ink: #111111;
    --white: #ffffff;
    --yellow: #f7ea1a;
    --frame: #f5b21b;
    --sky-top: #2b3f5c;
    --sky-mid: #5f7591;
    --city: #1a2233;
    --water: #6b5a3c;
    --glow: #c99a4a;
    --shore: #15130f;
  }
  * { margin: 0; padding: 0; box-sizing: border-box; }
  html, body { width: 1200px; height: 1050px; overflow: hidden; background: var(--paper); }
  .canvas { position: relative; width: 1200px; height: 1050px; background: var(--paper); }

  .designer-note {
    position: absolute; font-family: "Libre Baskerville", Georgia, serif;
    color: var(--ink); font-size: 19.5px; line-height: 24.5px;
  }
  .designer-note.top { left: 86px; top: 14px; }
  .designer-note.bottom { left: 56px; top: 916px; font-size: 21.5px; line-height: 29px; }
  .designer-note .gap { display: inline-block; width: 32px; }

  .postcard {
    position: absolute; left: 49px; top: 141px; width: 1047px; height: 750px; overflow: hidden;
  }
  .skyline-photo {
    position: absolute; inset: 0;
    background: linear-gradient(180deg, var(--sky-top) 0%, var(--sky-mid) 28%, #8494a8 40%, var(--city) 55%, var(--water) 66%, var(--glow) 73%, #3d3a36 84%, var(--shore) 100%);
  }

  .postcard > .txt { position: absolute; white-space: nowrap; }
  .dba { left: 31px; top: 34px; font-family: "Montserrat", Arial, sans-serif; font-weight: 700; font-size: 24px; color: var(--white); }

  .headline {
    left: 30px; top: 78px; width: 1000px; text-align: center; transform: rotate(-4.5deg);
    font-family: "Montserrat", Arial, sans-serif; font-weight: 800; color: var(--yellow);
    text-shadow: 6px 8px 10px rgba(0,0,0,0.75); line-height: 44px;
  }
  .headline .line1 { font-size: 34px; letter-spacing: 2px; display: block; margin-left: -80px; }
  .headline .line2 { font-size: 40px; letter-spacing: 2px; display: block; }

  .locate {
    left: 613px; top: 172px; width: 400px; text-align: center;
    font-family: "Open Sans", Arial, sans-serif; font-weight: 700; font-size: 21px; line-height: 32px; color: var(--white);
  }

  .services {
    left: 30px; top: 200px; list-style: none;
    font-family: "Open Sans", Arial, sans-serif; font-weight: 700; font-size: 19.5px; line-height: 29.4px; color: var(--white);
  }
  .services .spacer { height: 29px; }

  .tagline {
    left: 347px; top: 270px; width: 700px; text-align: center;
    font-family: "Roboto Condensed", "Arial Narrow", sans-serif; font-weight: 700; font-size: 50px; line-height: 62px; color: var(--white);
    text-shadow: 0 2px 4px rgba(0,0,0,0.5);
  }

  .role {
    left: 600px; top: 432px; width: 420px; text-align: center; transform: rotate(-6deg);
    font-family: "Montserrat", Arial, sans-serif; font-weight: 800; font-size: 27px; line-height: 38px; color: var(--yellow);
    text-shadow: 4px 6px 8px rgba(0,0,0,0.7);
  }

  .phone { left: 30px; top: 580px; font-family: "Open Sans", Arial, sans-serif; font-weight: 700; font-size: 40px; color: var(--yellow); }
  .contact {
    left: 30px; top: 642px; font-family: "Open Sans", Arial, sans-serif; font-weight: 700; font-size: 18.5px; line-height: 27px; color: var(--white);
  }

  .logo-box {
    position: absolute; left: 787px; top: 545px; width: 231px; height: 171px;
    background: var(--white); border: 11px solid var(--frame);
    display: flex; flex-direction: column; align-items: center; justify-content: center; gap: 12px;
  }
  .logo-box .mark { width: 34px; height: 34px; background: #1a1a1a; }
  .logo-box .name {
    font-family: "Open Sans", Arial, sans-serif; font-weight: 700; font-size: 22px; color: #1a1a1a; text-align: center; line-height: 26px;
  }
</style>
</head>
<body>
<div class="canvas">
  <p class="designer-note top">
    The jpg image files were taken from your website and are not<br>
    the correct DPI and resolution for quality printing.<br>
    For quality printing please&nbsp; upload correct resolution for your images!<br>
    Logo cannot be centered. It is cropped and presented from the website, Thanks!
  </p>

  <section class="postcard">
    <div class="skyline-photo" role="img" aria-label="Night skyline of Louisville across the river, city lights reflected in the water, tree branches at the left"></div>

    <p class="txt dba">D/B/A Bramblegate Dispatch Private Process Service</p>

    <h1 class="txt headline">
      <span class="line1">NOW SERVES</span>
      <span class="line2">LOUISVILLE AND LEXINGTON KY!</span>
    </h1>

    <p class="txt locate">locate missing persons:<br>parties to a lawsuit, witnesses,<br>heirs, or loved ones.</p>

    <ul class="txt services">
      <li>Marital investigations</li>
      <li>Criminal Defense Investigations</li>
      <li>Crime scene reconstruction</li>
      <li>Bloodstain pattern analysis</li>
      <li class="spacer"></li>
      <li>Civil Investigations</li>
      <li>injury claims</li>
      <li>Liability investigations</li>
      <li>Day-in-the-life videos</li>
      <li>asset investigations</li>
      <li>Background Screening</li>
      <li>Pre-employment and tenant screening.</li>
      <li>Missing Persons</li>
    </ul>

    <h2 class="txt tagline">FINDING THE EVIDENCE<br>YOU NEED TO WIN YOUR CASE!</h2>

    <p class="txt role">PRIVATE INVESTIGATORS<br>AND&nbsp; PROCESS SERVERS</p>

    <p class="txt phone">Tel: (555)014-2290</p>
    <p class="txt contact">
      48 E. Harlan Ave. Ste. 700 Louisville, KY.<br>
      112 N. Elm Row Suite 205, Louisville, KY 40299<br>
      website www.swiftpaperdeliveryagentsonline.com
    </p>

    <div class="logo-box">
      <span class="mark"></span>
      <span class="name">Wexmoor Inquiries</span>
    </div>
  </section>

  <p class="designer-note bottom">
    Anything I can help you with and design questions or corrections please<br>
    contact Theo<span class="gap"></span>theo.layouts@example.com
  </p>
</div>
</body>
</html>
```